Business Folder

I need a fresh, modern design for a business folder. I have our company's colors, logo, and a separate file for just the graphic part of our logo as a design element. No photo, just colors, gradients, and shadows to create depth. I like the idea of a rich grey as the background, however, I realize we'd have to lighten to 'Tax Advisory Services' part of our logo.

The design would just be the 'front' or outside of the folder from Mellowfax. Design file attached. You can find that here under 9 x 12 standard folder, Left and Right Pockets With Slit Both Sides:

https://www.mellowfax-example.com/content.html?id=folderDownloadTemplates&rightMenuId=rightMenu&footerId=bodyFooterStyle6

```html
<!DOCTYPE html>
<html lang="en">
<head>
<meta charset="utf-8">
<title>Tavrenna Tax Advisory Services – Presentation Folder</title>
<link href="https://fonts.googleapis.com/css2?family=Montserrat:wght@300;400;500;600;800&display=swap" rel="stylesheet">
<style>
  :root {
    --stage: #8a8a8a;
    --ink: #1f1f22;
    --charcoal: #202023;
    --charcoal-soft: #2b2b2f;
    --brand-blue: #1d4f7c;
    --brand-sky: #3fb3e0;
    --paper: #ffffff;
    --pocket-grey: #d8d9db;
    --watermark: rgba(0,0,0,0.06);
    --muted: #555558;
  }
  * { box-sizing: border-box; margin: 0; padding: 0; }
  html, body { width: 1200px; height: 1200px; overflow: hidden; }
  body {
    background: var(--stage);
    font-family: "Montserrat", sans-serif;
    position: relative;
  }
  .panel { position: absolute; box-shadow: 0 6px 18px rgba(0,0,0,0.35); overflow: hidden; }

  /* Shared brand lockup: name set in the piece's text font, one square beside it */
  .brand-lockup { display: inline-flex; flex-direction: column; align-items: flex-start; }
  .brand-name {
    display: flex; align-items: center; gap: 10px;
    font-weight: 800; font-size: 36px; line-height: 1; color: var(--brand-blue); letter-spacing: 1px;
  }
  .brand-square { width: 16px; height: 16px; background: var(--brand-sky); flex: none; }
  .brand-descriptor {
    font-weight: 400; font-size: 10px; letter-spacing: 1.5px; color: var(--muted);
    margin-top: 6px; padding-left: 26px; white-space: nowrap;
  }

  /* Front cover */
  .front-cover {
    left: 60px; top: 70px; width: 400px; height: 530px;
    background: linear-gradient(160deg, #d6d6d8 0%, #eeeeef 45%, var(--paper) 80%);
  }
  .front-cover .brand-lockup { position: absolute; left: 50px; top: 78px; }
  .headline-lead {
    position: absolute; left: 50px; top: 192px;
    font-weight: 300; font-size: 34px; color: #333; letter-spacing: 1px; white-space: nowrap;
  }
  .headline-band {
    position: absolute; left: 40px; top: 238px; width: 320px; height: 66px;
    background: var(--ink); color: var(--paper);
    font-weight: 800; font-size: 44px; letter-spacing: 2px;
    display: flex; align-items: center; justify-content: center;
  }
  .tagline {
    position: absolute; left: 50px; top: 318px;
    font-weight: 500; font-size: 15px; color: var(--brand-blue); white-space: nowrap;
  }
  .cover-url {
    position: absolute; right: 36px; bottom: 40px;
    font-weight: 500; font-size: 12px; color: #333;
  }

  /* Back cover */
  .back-cover {
    left: 740px; top: 70px; width: 400px; height: 530px;
    background: linear-gradient(150deg, var(--charcoal) 0%, var(--charcoal-soft) 55%, var(--charcoal) 100%);
  }
  .back-url {
    position: absolute; left: 0; right: 0; bottom: 50px; text-align: center;
    font-weight: 500; font-size: 13px; color: var(--paper);
  }

  /* Inside spread */
  .inside-spread { left: 220px; top: 650px; width: 760px; height: 500px; display: flex; background: var(--paper); }
  .inside-half { position: relative; width: 380px; height: 100%; }
  .inside-left { background: var(--paper); border-right: 2px solid #ddd; }
  .inside-right { background: linear-gradient(90deg, #b9b9bb 0%, #f1f1f2 45%, var(--paper) 75%); }
  .faint-mark {
    position: absolute; left: 0; right: 0; top: 238px; text-align: center; color: var(--watermark);
  }
  .faint-mark .mark-name { font-weight: 800; font-size: 40px; line-height: 1; letter-spacing: 2px; }
  .faint-mark .mark-descriptor { font-weight: 400; font-size: 12px; letter-spacing: 2px; margin-top: 6px; }
  .pocket { position: absolute; bottom: 0; height: 170px; }
  .pocket-dark {
    left: 0; right: 14px;
    background: linear-gradient(150deg, var(--charcoal) 0%, var(--charcoal-soft) 60%, var(--charcoal) 100%);
    border-top-right-radius: 14px;
    display: flex; align-items: center; justify-content: center;
    color: var(--paper); font-weight: 600; font-size: 16px;
  }
  .pocket-light {
    left: 14px; right: 0;
    background: var(--pocket-grey); border-top-left-radius: 14px;
    display: flex; align-items: center; justify-content: center;
  }
  .pocket-light .brand-name { font-size: 36px; }
  .pocket-light .brand-descriptor { font-size: 10px; color: var(--brand-blue); }
</style>
</head>
<body>
  <section class="panel front-cover" aria-label="Folder front cover">
    <div class="brand-lockup">
      <div class="brand-name"><span class="brand-square"></span>TAVRENNA</div>
      <div class="brand-descriptor">TAX ADVISORY SERVICES</div>
    </div>
    <p class="headline-lead">COMMITTED TO</p>
    <p class="headline-band">SOLUTIONS</p>
    <p class="tagline">A Present And Future Business Service</p>
    <p class="cover-url">www.tavrennataxadvisory.com</p>
  </section>

  <section class="panel back-cover" role="img" aria-label="Folder back cover: charcoal field with large faint geometric brand decoration">
    <p class="back-url">www.tavrennataxadvisory.com</p>
  </section>

  <section class="panel inside-spread" aria-label="Folder inside with left and right pockets">
    <div class="inside-half inside-left">
      <div class="faint-mark"><div class="mark-name">TAVRENNA</div><div class="mark-descriptor">TAX ADVISORY SERVICES</div></div>
      <div class="pocket pocket-dark" role="img" aria-label="Left pocket: charcoal with faint geometric decoration">www.tavrennataxadvisory.com</div>
    </div>
    <div class="inside-half inside-right">
      <div class="faint-mark"><div class="mark-name">TAVRENNA</div><div class="mark-descriptor">TAX ADVISORY SERVICES</div></div>
      <div class="pocket pocket-light">
        <div class="brand-lockup">
          <div class="brand-name"><span class="brand-square"></span>TAVRENNA</div>
          <div class="brand-descriptor">TAX ADVISORY SERVICES</div>
        </div>
      </div>
    </div>
  </section>
</body>
</html>
```